New Alcoholic Spiked Seltzer Line

We need a can design for a line of low calorie alcoholic seltzer. This product is a sparkling water and vodka drink with no sugar added in a slim 12 oz can.

This is a lighter, healthier, alternative to the sugary ready-to-drinks on the market. The product contains only 3 ingredients: Vodka, Water and Natural Flavors. It has only 100 calories but still has 5% alcohol, so you don't need to sacrifice alcohol to cut calories.

This product also does not contain any preservatives.

We want this design to communicate the following objectives to the consumer and in this order:

1. Appetizing product
2.Low calorie
3.Communicate the type of beverage (Spiked Seltzer)

The brand name of the product is VELKA.

The flavor of the product needed to be used for the design is Mango-Orange.

Comparable products are:

www.brisavelfizz.example/
https://www.tarnowbubble.example
https://quellrind.example/

The designs should not infringe or copy the creative directions of the products mentionned above. They are only given so that you can better understand the type of product we are developing.

Target Market(s)

Young Professional women between the ages of 25 and 44

Industry/Entity Type

Product

Colors

Designer to choose colors to be used in the design.

Requirements
Must have
• Design extendibility, meaning it can be adapted for other flavors.
• This is a new category in the market we are targeting, so consumers must easily be able to identify what type of product this is.

```html
<!DOCTYPE html>
<html lang="en">
<head>
<meta charset="utf-8">
<title>VELKA Spiked Seltzer – Mango Orange Can Label</title>
<link rel="stylesheet" href="https://fonts.googleapis.com/css2?family=Tinos:wght@400;700&display=swap">
<style>
  :root {
    --backdrop: #eef0f2;
    --orange: #e9542d;
    --orange-deep: #c93c1c;
    --silver-light: #ffffff;
    --silver-mid: #e4e6e8;
    --silver-dark: #c9cccf;
    --brand-grey: #8b8b8b;
    --white: #ffffff;
  }
  * { margin: 0; padding: 0; box-sizing: border-box; }
  html, body {
    width: 1199px;
    height: 1200px;
    overflow: hidden;
    background: var(--backdrop);
  }
  .canvas {
    position: relative;
    width: 1199px;
    height: 1200px;
  }
  .label {
    position: absolute;
    left: 360px;
    top: 30px;
    width: 480px;
    height: 1140px;
    overflow: hidden;
    font-family: "Tinos", "Times New Roman", serif;
  }
  .label-art {
    position: absolute;
    inset: 0;
    width: 480px;
    height: 1140px;
  }
  .calorie-claim {
    position: absolute;
    top: 24px;
    left: 0;
    width: 100%;
    text-align: center;
    color: var(--white);
    font-weight: 700;
    font-size: 31px;
    line-height: 1.2;
    letter-spacing: 0.5px;
  }
  .brand-name {
    position: absolute;
    top: 800px;
    left: 0;
    width: 100%;
    text-align: center;
    color: var(--brand-grey);
    font-weight: 400;
    font-size: 122px;
    line-height: 1;
    letter-spacing: -2px;
    white-space: nowrap;
  }
  .product-type {
    position: absolute;
    top: 944px;
    left: 0;
    width: 100%;
    text-align: center;
    color: var(--brand-grey);
    font-size: 44px;
    line-height: 1;
    letter-spacing: 1px;
    white-space: nowrap;
  }
  .volume-row {
    position: absolute;
    top: 1038px;
    left: 24px;
    right: 24px;
    display: flex;
    justify-content: space-between;
    color: var(--white);
    font-size: 22px;
    line-height: 1;
  }
  .claims-strip {
    position: absolute;
    top: 1100px;
    left: 0;
    width: 100%;
    text-align: center;
    color: var(--white);
    font-size: 12.5px;
    line-height: 1.2;
    white-space: nowrap;
    overflow: hidden;
  }
</style>
</head>
<body>
<main class="canvas">
  <section class="label">
    <svg class="label-art" viewBox="0 0 480 1140" xmlns="http://www.w3.org/2000/svg">
      <defs>
        <linearGradient id="silverBody" x1="0" y1="0" x2="1" y2="0">
          <stop offset="0" stop-color="#c9cccf"/>
          <stop offset="0.35" stop-color="#ffffff"/>
          <stop offset="0.7" stop-color="#e4e6e8"/>
          <stop offset="1" stop-color="#c9cccf"/>
        </linearGradient>
        <linearGradient id="orangeBand" x1="0" y1="0" x2="1" y2="0">
          <stop offset="0" stop-color="#c93c1c"/>
          <stop offset="0.4" stop-color="#e9542d"/>
          <stop offset="1" stop-color="#c93c1c"/>
        </linearGradient>
        <radialGradient id="fruitTones" cx="0.5" cy="0.55" r="0.6">
          <stop offset="0" stop-color="#f7a532"/>
          <stop offset="0.55" stop-color="#f2c07a"/>
          <stop offset="1" stop-color="#eef0f0"/>
        </radialGradient>
      </defs>
      <rect class="label-body" x="0" y="0" width="480" height="1140" fill="url(#silverBody)"/>
      <polygon class="label-top-band" points="0,0 480,0 480,71 240,134 0,71" fill="url(#orangeBand)"/>
      <g role="img" aria-label="Illustration of a halved orange and a mango with green leaves, ice cubes and a water splash">
        <polygon class="fruit-illustration" points="20,229 460,229 460,703 240,798 20,703" fill="url(#fruitTones)"/>
      </g>
      <polyline points="0,712 240,806 480,712" fill="none" stroke="#c9cccf" stroke-width="2"/>
      <polygon class="label-bottom-band" points="0,1010 240,1075 480,1010 480,1140 0,1140" fill="url(#orangeBand)"/>
    </svg>
    <p class="calorie-claim">ONLY 100 CALORIES</p>
    <h1 class="brand-name">VELKA</h1>
    <p class="product-type">SPIKED SELTZER</p>
    <div class="volume-row"><span>Alc 5%</span><span>12 oz</span></div>
    <p class="claims-strip">NO PRESERVATIVES ● NO SUGAR ● NO PRESERVATIVES ● NO SUGAR</p>
  </section>
</main>
</body>
</html>
```